70s 80s Revival club night

Hi,

I'm look for a poster design for a 70s & 80s revival club night.
The design must say thr following...

Copper Kites
70s & 80s Revival Club Night.

Also, must incorporate our company logo (Attached)

```html
<!DOCTYPE html>
<html lang="en">
<head>
<meta charset="utf-8">
<title>70's &amp; 80's Revival Club Night</title>
<link href="https://fonts.googleapis.com/css2?family=Shrikhand&family=Bebas+Neue&family=Oswald:wght@200;300;400;500;600&display=swap" rel="stylesheet">
<style>
  :root {
    --paper: #ffffff;
    --sand-edge: #cfc7b8;
    --sand-mid: #e3ddd2;
    --sand-light: #f6f4f0;
    --brown: #4f3a1b;
    --brown-soft: #7a6242;
    --cream-outline: #f3e2c9;
    --ribbon: #3d3b39;
    --ribbon-dark: #242322;
    --ink: #2f2b26;
    --art-light: #a7a196;
    --art-dark: #5c574f;
  }
  * { box-sizing: border-box; margin: 0; padding: 0; }
  html, body { width: 750px; height: 1200px; overflow: hidden; background: var(--paper); }
  .poster {
    position: relative;
    width: 750px;
    height: 1200px;
    background: var(--paper);
  }
  .poster-field {
    position: absolute;
    left: 17px; top: 20px; right: 18px; bottom: 20px;
    background: radial-gradient(ellipse at 50% 62%, var(--sand-light) 0%, var(--sand-mid) 55%, var(--sand-edge) 100%);
  }
  .headline-decades {
    position: absolute;
    top: 90px; left: 0; width: 750px;
    text-align: center;
    font-family: "Shrikhand", cursive;
    font-size: 58px;
    line-height: 1;
    color: var(--brown);
    text-shadow: 2px 2px 0 var(--cream-outline);
  }
  .headline-decades .amp { font-size: 34px; vertical-align: 6px; }
  .headline-main {
    position: absolute;
    top: 166px; left: 0; width: 750px;
    text-align: center;
    font-family: "Shrikhand", cursive;
    font-size: 118px;
    line-height: 1;
    letter-spacing: 1px;
    color: var(--brown);
    text-shadow: 3px 3px 0 var(--cream-outline);
  }
  .ribbon {
    position: absolute;
    top: 288px; left: 175px;
    width: 400px; height: 80px;
  }
  .ribbon-label {
    position: absolute;
    top: 296px; left: 0; width: 750px;
    text-align: center;
    font-family: "Bebas Neue", sans-serif;
    font-size: 50px;
    letter-spacing: 2px;
    line-height: 60px;
    color: #ffffff;
  }
  .boombox-art {
    position: absolute;
    top: 402px; left: 64px;
    width: 612px; height: 282px;
    border-radius: 10px;
    background: linear-gradient(180deg, var(--art-light) 0%, var(--art-dark) 100%);
  }
  .rule {
    position: absolute;
    left: 214px; width: 326px; height: 2px;
    background: var(--brown-soft);
  }
  .rule-top { top: 731px; }
  .rule-bottom { top: 884px; }
  .date-day {
    position: absolute;
    top: 746px; left: 208px;
    font-family: "Shrikhand", cursive;
    font-size: 112px;
    line-height: 1;
    color: var(--brown);
  }
  .date-detail {
    position: absolute;
    top: 752px; left: 392px;
    color: var(--brown);
  }
  .date-weekday {
    font-family: "Bebas Neue", sans-serif;
    font-size: 44px;
    line-height: 42px;
  }
  .date-month {
    font-family: "Oswald", sans-serif;
    font-weight: 200;
    font-size: 38px;
    line-height: 44px;
  }
  .date-time {
    font-family: "Oswald", sans-serif;
    font-weight: 500;
    font-size: 15px;
    letter-spacing: 1px;
    line-height: 22px;
  }
  .features {
    position: absolute;
    top: 928px; left: 0; width: 750px;
    display: flex;
    justify-content: center;
    gap: 40px;
    font-family: "Oswald", sans-serif;
    font-weight: 500;
    font-size: 18px;
    letter-spacing: 3px;
    color: var(--ink);
  }
  .features .divider { letter-spacing: 0; }
  .headliner {
    position: absolute;
    top: 962px; left: 0; width: 750px;
    text-align: center;
    font-family: "Oswald", sans-serif;
    font-size: 32px;
    color: var(--ink);
  }
  .headliner .headliner-name { color: var(--brown); font-weight: 500; }
  .headliner .headliner-role { font-weight: 200; }
  .brand {
    position: absolute;
    top: 1076px; left: 0; width: 750px;
    display: flex;
    align-items: center;
    justify-content: center;
    gap: 10px;
  }
  .brand-square { width: 22px; height: 22px; background: var(--ink); }
  .brand-name {
    font-family: "Oswald", sans-serif;
    font-weight: 600;
    font-size: 30px;
    line-height: 40px;
    letter-spacing: 1px;
    color: var(--ink);
  }
  .brand-tagline {
    position: absolute;
    top: 1120px; left: 0; width: 750px;
    display: flex;
    align-items: center;
    justify-content: center;
    gap: 6px;
    font-family: "Oswald", sans-serif;
    font-weight: 500;
    font-size: 11px;
    letter-spacing: 2px;
    color: var(--ink);
  }
  .brand-tagline .tag-line { width: 40px; height: 1px; background: var(--ink); }
</style>
</head>
<body>
<main class="poster">
  <div class="poster-field"></div>

  <h1 class="headline-decades">70'S <span class="amp">&amp;</span> 80'S</h1>
  <h2 class="headline-main">REVIVAL</h2>

  <svg class="ribbon" viewBox="0 0 400 80" aria-hidden="true">
    <polygon points="0,22 58,22 58,72 0,72 18,47" fill="var(--ribbon)"/>
    <polygon points="400,22 342,22 342,72 400,72 382,47" fill="var(--ribbon)"/>
    <polygon points="47,62 58,72 58,62" fill="var(--ribbon-dark)"/>
    <polygon points="353,62 342,72 342,62" fill="var(--ribbon-dark)"/>
    <rect x="47" y="4" width="306" height="58" fill="var(--ribbon)"/>
  </svg>
  <div class="ribbon-label">CLUB NIGHT</div>

  <div class="boombox-art" role="img" aria-label="Illustration of a retro boombox with a cassette tape on the left and a vinyl record on the right"></div>

  <div class="rule rule-top"></div>
  <div class="date-day">23</div>
  <div class="date-detail">
    <div class="date-weekday">SATURDAY</div>
    <div class="date-month">JANUARY</div>
    <div class="date-time">4PM - 9PM</div>
  </div>
  <div class="rule rule-bottom"></div>

  <div class="features">
    <span>DRINK SPECIALS</span>
    <span class="divider">|</span>
    <span>DJ MIXER</span>
    <span class="divider">|</span>
    <span>DANCE PARTY</span>
  </div>

  <div class="headliner"><span class="headliner-role">DJ</span> <span class="headliner-name">RAY</span></div>

  <div class="brand">
    <span class="brand-square"></span>
    <span class="brand-name">COPPER KITES</span>
  </div>
  <div class="brand-tagline">
    <span class="tag-line"></span>
    <span>SPIN TIL SUNRISE</span>
    <span class="tag-line"></span>
  </div>
</main>
</body>
</html>
```